Criação de Cartao de Visita para Vigor & Equilíbrio
" Venda de Suplementos Alimentares/Nutricionais, principalmente via whatsapp e facebook, fazemos entregas e aceitamos cartões. Ainda não possuimos loja física. Cobrimos qualquer oferta de site ou loja nacional. "

```html
<!DOCTYPE html>
<html lang="pt-BR">
<head>
<meta charset="UTF-8">
<title>Vigor &amp; Equilíbrio — Cartão de Visita</title>
<link href="https://fonts.googleapis.com/css2?family=Exo+2:ital,wght@1,800&family=Montserrat:wght@400;500&display=swap" rel="stylesheet">
<style>
  :root {
    --bg: #e9e7e4;
    --card-black: #0b0b0b;
    --card-white: #ffffff;
    --gold: #f2b418;
    --orange: #f08a12;
    --text-light: #f2f2f2;
    --text-muted: #bdbdbd;
    --text-dark: #1a1a1a;
  }
  * { box-sizing: border-box; margin: 0; padding: 0; }
  html, body { width: 1200px; height: 1200px; overflow: hidden; }
  body {
    background: var(--bg);
    display: flex;
    flex-direction: column;
    align-items: center;
    justify-content: center;
    gap: 90px;
    font-family: "Montserrat", sans-serif;
  }
  .card {
    width: 880px;
    height: 500px;
    border-radius: 30px;
    overflow: hidden;
    position: relative;
    box-shadow: 0 14px 30px rgba(0,0,0,0.18);
  }
  /* Verso: informações */
  .card--info { display: flex; background: var(--card-black); }
  .card--info .brand-side {
    width: 47%;
    background: var(--card-white);
    display: flex;
    flex-direction: column;
    align-items: center;
    justify-content: center;
    gap: 26px;
    border-right: 5px solid var(--orange);
  }
  .contact-side {
    flex: 1;
    padding: 50px 48px 0 30px;
    color: var(--text-light);
    text-align: right;
  }
  .person-name { font-size: 20px; letter-spacing: 3px; font-weight: 500; }
  .person-role { font-size: 12px; letter-spacing: 2px; color: var(--text-muted); margin-top: 6px; }
  .contact-list { list-style: none; margin-top: 70px; display: flex; flex-direction: column; gap: 15px; }
  .contact-list li {
    font-size: 15px;
    display: flex;
    justify-content: flex-end;
    align-items: center;
    gap: 14px;
  }
  .contact-list svg { width: 16px; height: 16px; flex: none; }
  /* Frente: marca */
  .card--brand {
    background: var(--card-black);
    display: flex;
    flex-direction: column;
    align-items: center;
    justify-content: center;
    gap: 34px;
  }
  .card--brand::after {
    content: "";
    position: absolute;
    left: 0; right: 0; bottom: 0;
    height: 18px;
    background: linear-gradient(to right, var(--gold), var(--orange));
  }
  .brand-mark {
    border-radius: 50%;
    background: var(--gold);
  }
  .brand-side .brand-mark { width: 130px; height: 130px; }
  .card--brand .brand-mark { width: 170px; height: 170px; }
  .brand-name {
    font-family: "Exo 2", sans-serif;
    font-weight: 800;
    font-style: italic;
    text-transform: uppercase;
    color: var(--orange);
  }
  .brand-side .brand-name { font-size: 30px; }
  .card--brand .brand-name { font-size: 46px; }
</style>
</head>
<body>

  <section class="card card--info">
    <div class="brand-side">
      <div class="brand-mark"></div>
      <div class="brand-name">Vigor &amp; Equilíbrio</div>
    </div>
    <div class="contact-side">
      <p class="person-name">NOME SOBRENOME</p>
      <p class="person-role">FUNÇÃO</p>
      <ul class="contact-list">
        <li>Rua do Projeto, 000, Cidade/Estado
          <svg viewBox="0 0 16 16"><rect width="16" height="16" rx="2" fill="#f08a12"/><path d="M8 3a3 3 0 0 0-3 3c0 2.3 3 6 3 6s3-3.7 3-6a3 3 0 0 0-3-3z" fill="#0b0b0b"/></svg>
        </li>
        <li>(00) 0000-0000
          <svg viewBox="0 0 16 16"><rect width="16" height="16" rx="2" fill="#f08a12"/><path d="M5 3.5l2 2-1 1.2c.6 1.3 1.6 2.3 2.9 2.9l1.1-1 2 2-1.2 1.4C7.6 12 4 8.4 3.6 5.2z" fill="#0b0b0b"/></svg>
        </li>
        <li>(00) 0000-0000
          <svg viewBox="0 0 16 16"><rect width="16" height="16" rx="2" fill="#f08a12"/><rect x="5" y="3" width="6" height="10" rx="1" fill="#0b0b0b"/></svg>
        </li>
        <li>contato@vigorequilibrio.com.br
          <svg viewBox="0 0 16 16"><rect width="16" height="16" rx="2" fill="#f08a12"/><rect x="3" y="5" width="10" height="7" fill="#0b0b0b"/><path d="M3 5l5 4 5-4" stroke="#f08a12" fill="none"/></svg>
        </li>
        <li>www.vigorequilibrio.com.br
          <svg viewBox="0 0 16 16"><rect width="16" height="16" rx="2" fill="#f08a12"/><circle cx="8" cy="8" r="4.5" fill="none" stroke="#0b0b0b" stroke-width="1.5"/><path d="M3.5 8h9" stroke="#0b0b0b" stroke-width="1.2"/></svg>
        </li>
      </ul>
    </div>
  </section>

  <section class="card card--brand">
    <div class="brand-mark"></div>
    <div class="brand-name">Vigor &amp; Equilíbrio</div>
  </section>

</body>
</html>
```